Business Card Design

I would like a new business card design for an accounting firm that specializes in resolving clients tax problems. I want the card to give the impression that we are not your typical stodgy accounting firm, but at the same time we will get the job done.
Industry/Entity Type
Business
Contact Information for Business Card
Dorian T Welsby
Certified Public Accountant
38-27 52nd Street
Sunnyside, NY 11287
Tel: (718) 555-0142
Fax: (888) 555-0199
e-mail: dtwthecpa@ledgerpost.com
website: harborfilingreliefexperts.com

```html
<!DOCTYPE html>
<html lang="en">
<head>
<meta charset="utf-8">
<title>Business Card</title>
<link href="https://fonts.googleapis.com/css2?family=Lato:wght@400;700&display=swap" rel="stylesheet">
<style>
  :root {
    --backdrop: #eceded;
    --card: #1c1c1d;
    --card-edge: #232324;
    --accent: #f04a1c;
    --tag-front: #f7a21b;
    --tag-back: #ea5a26;
    --ink: #ffffff;
    --ink-soft: #d9d9d9;
  }
  * { margin: 0; padding: 0; box-sizing: border-box; }
  html, body {
    width: 1200px;
    height: 1039px;
    overflow: hidden;
    background: var(--backdrop);
    font-family: "Lato", Arial, sans-serif;
  }
  .stage {
    width: 1200px;
    height: 1039px;
    display: flex;
    align-items: center;
    justify-content: center;
  }
  .card {
    position: relative;
    width: 840px;
    height: 480px;
    background: var(--card);
    box-shadow: 0 18px 40px rgba(0,0,0,.25);
    overflow: hidden;
  }
  .corner-bar { position: absolute; background: var(--accent); }
  .corner-bar--top { top: 0; right: 0; width: 360px; height: 14px; }
  .corner-bar--right { top: 0; right: 0; width: 14px; height: 70px; }
  .corner-bar--bottom { bottom: 0; left: 0; width: 330px; height: 14px; }
  .corner-bar--left { bottom: 0; left: 0; width: 14px; height: 70px; }

  .tag-mark {
    position: absolute;
    left: 130px;
    top: 220px;
    width: 200px;
    height: 170px;
  }

  .details {
    position: absolute;
    left: 400px;
    top: 92px;
    color: var(--ink);
  }
  .name { font-size: 34px; font-weight: 400; letter-spacing: .3px; line-height: 1.1; }
  .title { font-size: 14px; color: var(--ink-soft); margin-top: 4px; }
  .address { font-size: 19px; line-height: 1.35; margin-top: 14px; }
  .contact-list { list-style: none; margin-top: 18px; }
  .contact-list li {
    display: flex;
    align-items: center;
    gap: 12px;
    font-size: 19px;
    line-height: 1;
    margin-bottom: 10px;
  }
  .contact-icon {
    width: 22px; height: 22px;
    flex: none;
  }
</style>
</head>
<body>
<main class="stage">
  <section class="card">
    <span class="corner-bar corner-bar--top"></span>
    <span class="corner-bar corner-bar--right"></span>
    <span class="corner-bar corner-bar--bottom"></span>
    <span class="corner-bar corner-bar--left"></span>

    <svg class="tag-mark" role="img" aria-label="Orange price tag illustration with a percent sign" viewBox="0 0 200 170">
      <rect x="28" y="40" width="160" height="115" rx="6" fill="var(--tag-back)"/>
      <rect x="10" y="18" width="160" height="115" rx="6" fill="var(--tag-front)"/>
    </svg>

    <div class="details">
      <h1 class="name">Name Here</h1>
      <p class="title">Title Here</p>
      <p class="address">Address line1, Address line2,<br>City, Zipcode</p>
      <ul class="contact-list">
        <li>
          <svg class="contact-icon" viewBox="0 0 22 22"><circle cx="11" cy="11" r="11" fill="var(--ink)"/><rect x="6" y="6" width="10" height="10" rx="2" fill="var(--card)"/><rect x="8" y="8" width="6" height="2" fill="var(--ink)"/></svg>
          000 000 0000
        </li>
        <li>
          <svg class="contact-icon" viewBox="0 0 22 22"><circle cx="11" cy="11" r="11" fill="var(--ink)"/><path d="M7 6c1-1 2 0 2.5 1.5l-1 1.2c.6 1.6 1.8 2.8 3.4 3.4l1.2-1c1.5.5 2.5 1.5 1.5 2.5-1 1.2-2.5 1.4-4.4.3C8.5 12.5 7 10.8 6.2 8.6 5.7 7.3 6 6.6 7 6z" fill="var(--card)"/></svg>
          000 000 0000
        </li>
        <li>
          <svg class="contact-icon" viewBox="0 0 22 22"><circle cx="11" cy="11" r="11" fill="var(--ink)"/><rect x="5.5" y="9" width="11" height="7" rx="1" fill="var(--card)"/><rect x="7.5" y="5.5" width="7" height="4" fill="var(--card)"/></svg>
          000 000 0000
        </li>
        <li>
          <svg class="contact-icon" viewBox="0 0 22 22"><circle cx="11" cy="11" r="11" fill="var(--ink)"/><rect x="5" y="7" width="12" height="8" rx="1" fill="var(--card)"/><path d="M5.5 7.5L11 11.5l5.5-4" stroke="var(--ink)" stroke-width="1.2" fill="none"/></svg>
          info@websitename.com
        </li>
        <li>
          <svg class="contact-icon" viewBox="0 0 22 22"><circle cx="11" cy="11" r="11" fill="var(--ink)"/><circle cx="11" cy="11" r="6" fill="none" stroke="var(--card)" stroke-width="1.5"/><path d="M5 11h12M11 5c-2.5 3-2.5 9 0 12M11 5c2.5 3 2.5 9 0 12" stroke="var(--card)" stroke-width="1.2" fill="none"/></svg>
          www.websitename.com
        </li>
      </ul>
    </div>
  </section>
</main>
</body>
</html>
```